Zielgruppe
Zielgruppe: M/W, 25-40 J., Unternehmer
Aufgabenstellung
Der Umfang für dieses Projekt besteht aus 3 Bannern in einem Style.
Banner 1: Online-Lösungen
Banner 2: Online-Services
Banner 3: Online-Marketing

```html
<!DOCTYPE html>
<html lang="de">
<head>
<meta charset="utf-8">
<title>Online Banner</title>
<link rel="stylesheet" href="https://fonts.googleapis.com/css2?family=Montserrat:wght@300;400&display=swap">
<style>
  :root {
    --frame: #cccccc;
    --paper: #ffffff;
    --ink: #1a1a1a;
    --blue-light: #0e80b2;
    --blue-dark: #003660;
    --icon-dark: #1e2a38;
    --icon-ring: #d8dadc;
    --accent-gold: #f2c200;
    --dot: #333333;
  }
  * { box-sizing: border-box; margin: 0; padding: 0; }
  html, body {
    width: 1200px;
    height: 1115px;
    overflow: hidden;
    background: var(--paper);
  }
  .canvas {
    position: relative;
    width: 1200px;
    height: 1115px;
  }
  .banner {
    position: absolute;
    left: 54px;
    width: 1071px;
    height: 272px;
    background: var(--frame);
  }
  .banner--solutions { top: 65px; }
  .banner--services { top: 415px; }
  .banner--marketing { top: 768px; }

  .banner__title-area {
    position: absolute;
    left: 18px;
    top: 18px;
    width: 1032px;
    height: 120px;
    background: var(--paper);
  }
  .banner__title {
    position: absolute;
    left: 16px;
    top: 26px;
    font-family: "Montserrat", sans-serif;
    font-weight: 300;
    font-size: 52px;
    letter-spacing: 1px;
    color: var(--ink);
    line-height: 1;
    white-space: nowrap;
  }
  .banner__band {
    position: absolute;
    left: 18px;
    top: 138px;
    width: 1032px;
    height: 116px;
    background: linear-gradient(90deg, var(--blue-light) 0%, #0a5f92 45%, var(--blue-dark) 100%);
  }
  .banner__tagline {
    position: absolute;
    left: 15px;
    top: 44px;
    font-family: "Montserrat", sans-serif;
    font-weight: 400;
    font-size: 22.5px;
    color: var(--paper);
    white-space: nowrap;
  }
  .banner__dots {
    position: absolute;
    left: 896px;
    top: 257px;
    width: 156px;
    height: 4px;
    background-image: radial-gradient(circle, var(--dot) 1.6px, transparent 2px);
    background-size: 14.2px 4px;
  }
  .banner__icon {
    position: absolute;
    left: 856px;
    top: 59px;
    width: 144px;
    height: 144px;
  }
</style>
</head>
<body>
<main class="canvas">

  <section class="banner banner--solutions">
    <div class="banner__title-area">
      <h2 class="banner__title">ONLINE | LÖSUNGEN</h2>
    </div>
    <div class="banner__band">
      <p class="banner__tagline">Erstellung von individuellen Online-Lösungen für Ihr E-Business</p>
    </div>
    <div class="banner__dots"></div>
    <svg class="banner__icon" viewBox="0 0 144 144" aria-hidden="true">
      <defs>
        <radialGradient id="ring-a" cx="50%" cy="35%" r="65%">
          <stop offset="0" stop-color="#ffffff"/><stop offset="1" stop-color="#b9bcc0"/>
        </radialGradient>
        <radialGradient id="core-a" cx="50%" cy="30%" r="70%">
          <stop offset="0" stop-color="#4a5868"/><stop offset="1" stop-color="#111a24"/>
        </radialGradient>
      </defs>
      <circle cx="72" cy="72" r="70" fill="url(#ring-a)"/>
      <circle cx="72" cy="72" r="56" fill="url(#core-a)"/>
      <path d="M72 34c-15 0-25 11-25 24 0 9 5 15 9 19 3 3 4 6 4 10h24c0-4 1-7 4-10 4-4 9-10 9-19 0-13-10-24-25-24z" fill="#f4f6f8"/>
      <path d="M66 86v-14l-5-8M78 86v-14l5-8M66 72h12" fill="none" stroke="#8a95a0" stroke-width="2"/>
      <rect x="61" y="89" width="22" height="5" rx="2" fill="#c8ccd0"/>
      <rect x="62" y="96" width="20" height="5" rx="2" fill="#c8ccd0"/>
      <rect x="65" y="103" width="14" height="5" rx="2" fill="#c8ccd0"/>
    </svg>
  </section>

  <section class="banner banner--services">
    <div class="banner__title-area">
      <h2 class="banner__title">ONLINE | SERVICES</h2>
    </div>
    <div class="banner__band">
      <p class="banner__tagline">Unsere Service-Dienstleistungen für Ihren Onlineshop</p>
    </div>
    <div class="banner__dots"></div>
    <svg class="banner__icon" viewBox="0 0 144 144" aria-hidden="true">
      <circle cx="72" cy="72" r="70" fill="url(#ring-a)"/>
      <circle cx="72" cy="72" r="56" fill="url(#core-a)"/>
      <text x="72" y="96" text-anchor="middle" font-family="Montserrat, sans-serif" font-weight="400" font-size="78" fill="var(--accent-gold)">@</text>
    </svg>
  </section>

  <section class="banner banner--marketing">
    <div class="banner__title-area">
      <h2 class="banner__title">ONLINE | MARKETING</h2>
    </div>
    <div class="banner__band">
      <p class="banner__tagline">Effiziente Online-Marketing-Komponenten für Ihr Unternehmen</p>
    </div>
    <div class="banner__dots"></div>
    <svg class="banner__icon" viewBox="0 0 144 144" aria-hidden="true">
      <circle cx="72" cy="72" r="70" fill="url(#ring-a)"/>
      <circle cx="72" cy="72" r="56" fill="url(#core-a)"/>
      <rect x="44" y="88" width="12" height="16" fill="#f4f6f8"/>
      <rect x="60" y="76" width="12" height="28" fill="#f4f6f8"/>
      <rect x="76" y="62" width="12" height="42" fill="#f4f6f8"/>
      <rect x="92" y="46" width="12" height="58" fill="#f4f6f8"/>
    </svg>
  </section>

</main>
</body>
</html>
```